Business Card - Rebranding for Consulting Firm

We are renaming and rebranding our consulting firm and need to raise the level of quality of our cards as part of that effort. We consult to leading high tech, life science and other innovation sector companies.

Need a two-sided business card design.

Side 1: (a) Company logo (b) tag line: Optimize Your Investment in Talent (c) Name (d) Title (e) Phone 1: Office (f) Phone 2: Mobile (g) email: person@HollowmereAdvisory.com

Side 2: Two lines of text: (a) Growth is Imperative. Change is Constant. Talent Executes Strategy. (b) We help you excel at all three.

Target Market(s)

Business and human resources executives and senior managers

Industry/Entity Type

Management Consulting

Contact Information for Business Card

Font styles to use
Sans Serif

Requirements
Must have
• clean, not too busy, but with a bit of creativity. Stick to the colors used in the attached logo
• appeal to high tech, life science companies
Nice to have
• prefer white background

```html
<!DOCTYPE html>
<html lang="en">
<head>
<meta charset="utf-8">
<title>Hollowmere Advisory – Business Card</title>
<link href="https://fonts.googleapis.com/css2?family=Open+Sans:wght@400;600;700&display=swap" rel="stylesheet">
<style>
  :root {
    --blue: #0a72b5;
    --blue-light: #1ea5de;
    --blue-dark: #0b5a8f;
    --ink: #2b2b2b;
    --grey: #555;
    --paper: #ffffff;
    --stage: #e9ecef;
  }
  * { box-sizing: border-box; margin: 0; padding: 0; }
  html, body { width: 1200px; height: 900px; overflow: hidden; }
  body {
    background: var(--stage);
    font-family: "Open Sans", Arial, sans-serif;
    position: relative;
  }
  .card {
    position: absolute;
    width: 560px;
    height: 320px;
    background: var(--paper);
    border-radius: 24px;
    overflow: hidden;
    box-shadow: 0 6px 18px rgba(0,0,0,.15);
  }
  .card-details { left: 320px; top: 70px; }
  .card-message { left: 320px; top: 500px; }

  .edge-band {
    position: absolute; left: 0; right: 0; bottom: 0; height: 10px;
    background: linear-gradient(90deg, var(--blue-dark), var(--blue-light));
  }

  /* brand mark */
  .brand { display: flex; align-items: center; gap: 8px; }
  .brand-square { width: 18px; height: 18px; background: var(--blue); flex: none; }
  .brand-name { color: var(--blue); font-weight: 600; font-size: 24px; letter-spacing: -.3px; white-space: nowrap; }

  /* details side */
  .card-details .brand { position: absolute; left: 36px; top: 40px; }
  .tagline {
    position: absolute; left: 36px; top: 80px;
    font-size: 10.5px; font-weight: 600; color: var(--grey);
    letter-spacing: .4px; text-transform: uppercase;
  }
  .person { position: absolute; right: 40px; top: 110px; text-align: right; }
  .person-name { font-size: 28px; font-weight: 700; letter-spacing: .5px; color: var(--ink); line-height: 1.1; }
  .person-name .surname { color: var(--blue-light); }
  .person-title { font-size: 12px; font-weight: 700; color: var(--grey); letter-spacing: 1px; margin-top: 2px; }

  .contacts { position: absolute; left: 210px; right: 0; top: 186px; list-style: none; }
  .contact {
    display: flex; align-items: center; gap: 12px;
    height: 34px; border-bottom: 2px solid var(--blue);
    font-size: 13px; color: var(--ink);
  }
  .contact:nth-child(3) { border-color: var(--blue-light); }
  .contact-icon {
    width: 28px; height: 28px; background: var(--blue);
    display: flex; align-items: center; justify-content: center; flex: none;
  }
  .contact:nth-child(3) .contact-icon { background: var(--blue-light); }
  .contact-icon svg { width: 18px; height: 18px; }

  /* message side */
  .card-message .brand { position: absolute; left: 0; right: 0; top: 92px; justify-content: center; gap: 14px; }
  .card-message .brand-square { width: 32px; height: 32px; }
  .card-message .brand-name { font-size: 44px; letter-spacing: -1px; }
  .message {
    position: absolute; left: 0; right: 0; top: 200px; text-align: center;
    color: var(--blue); font-weight: 600; font-size: 14px; line-height: 1.6;
  }
</style>
</head>
<body>

<section class="card card-details">
  <div class="brand">
    <span class="brand-square"></span>
    <span class="brand-name">Hollowmere Advisory</span>
  </div>
  <p class="tagline">Optimize your investment in talent</p>

  <div class="person">
    <h1 class="person-name">MARCUS <span class="surname">ELLERY</span></h1>
    <p class="person-title">GENERAL MANAGER</p>
  </div>

  <ul class="contacts">
    <li class="contact">
      <span class="contact-icon">
        <svg viewBox="0 0 24 24" fill="#fff"><path d="M6.6 10.8a15.1 15.1 0 0 0 6.6 6.6l2.2-2.2a1 1 0 0 1 1-.25 11.4 11.4 0 0 0 3.6.6 1 1 0 0 1 1 1V20a1 1 0 0 1-1 1A17 17 0 0 1 3 4a1 1 0 0 1 1-1h3.5a1 1 0 0 1 1 1c0 1.250.2 2.450.6 3.6a1 1 0 0 1-.25 1z"/></svg>
      </span>
      <span>+(555) 0142 368</span>
    </li>
    <li class="contact">
      <span class="contact-icon">
        <svg viewBox="0 0 24 24" fill="none" stroke="#fff" stroke-width="2"><rect x="7" y="2.5" width="10" height="19" rx="1.5"/><line x1="11" y1="18" x2="13" y2="18"/></svg>
      </span>
      <span>+(555) 0142 368</span>
    </li>
    <li class="contact">
      <span class="contact-icon">
        <svg viewBox="0 0 24 24" fill="none" stroke="#fff" stroke-width="1.8"><rect x="3" y="5.5" width="18" height="13"/><polyline points="3,6 12,13 21,6"/></svg>
      </span>
      <span>person@HollowmereAdvisory.com</span>
    </li>
  </ul>

  <div class="edge-band"></div>
</section>

<section class="card card-message">
  <div class="brand">
    <span class="brand-square"></span>
    <span class="brand-name">Hollowmere Advisory</span>
  </div>
  <p class="message">
    Growth is imperative | Change is constant | Talent executes strategy<br>
    We help you excel at all three
  </p>
  <div class="edge-band"></div>
</section>

</body>
</html>
```